The Mariposa - Print identity

The Mariposa is a mixed-use commercial/residential condo building in beautiful Vancouver. It is a fantastic exemple of mid-century modern architecture (built in 1955 as the HQ of the Northfield Power Works Corp., it was converted to condos in 1995) and has several valuable architectural elements. It is a landmark building in the downtown core.

Although we have a wordmark and other graphic collateral we need to retain, as we reorganized the management of the building we wish to refresh the print- (and online) communication with a splash of colour, professionalism and consistency to indicate things are now different. (Thus far it's been left to anyone to put together logos, fonts and colours sometimes to horrific results!)

We are very proud of our building and its heritage: please seek inspiration in the images attached.

Merci
Mathieu

Target Market(s)

Mid-30's professional downtown dwellers.
Values: Reliable, solid, well-managed, good value, long-lasting, sleek, clean, modern with an edge.

Industry/Entity Type

Real Estate

Requirements
Must have
• 1/ Reuse "The Mariposa" wordmark. Other collateral optional but simpler is better.
• 2/ Prepare at least one design for a letter-size (8.5X11) multi-purpose document (bulletin/memo/newsletter/letterhead) in colour & B/W versions.
Nice to have
• 1/ Design should be easily transferable to website and email newsletter.
• 2/ MS Word and/or html template would be nice rather than graphic file.
• 3/ Font/size, layout, titles and formatting suggestions would be awesome to make suitable for 'sample usage' docs provided.
• 4/ Option to include/exclude sender address depending if used for letterhead or bulletin/newsletter
• 5/ Building is managed by 3rd party - include footnote or sidebar with "Proudly managed by BrenTor Coastal. Lou Dane, Senior Property Manager" type of mention (no vector logo file currently available, use placeholder)

```html
<!DOCTYPE html>
<html lang="en">
<head>
<meta charset="utf-8">
<title>The Mariposa — Letterhead</title>
<link rel="stylesheet" href="https://fonts.googleapis.com/css2?family=Oswald:wght@300&display=swap">
<style>
  :root {
    --paper: #ffffff;
    --ink: #1c1c1c;
    --slate: #4b6a7b;
    --sage: #7e8a81;
    --frame: #dce3e6;
  }
  * { margin: 0; padding: 0; box-sizing: border-box; }
  html, body { width: 928px; height: 1200px; overflow: hidden; background: var(--paper); }
  .letterhead {
    position: relative;
    width: 928px;
    height: 1200px;
    background: var(--paper);
    font-family: "Oswald", "Arial Narrow", sans-serif;
    font-weight: 300;
    color: var(--ink);
  }
  .wordmark {
    position: absolute;
    left: 78px;
    top: 38px;
    font-size: 52px;
    letter-spacing: 4px;
    line-height: 1;
    text-transform: uppercase;
    color: var(--ink);
  }
  .header-mosaic {
    position: absolute;
    right: 0;
    top: 0;
    width: 414px;
    height: 134px;
    background: linear-gradient(100deg, var(--sage) 0%, var(--slate) 45%, #3a4a52 75%, var(--sage) 100%);
  }
  .content-frame {
    position: absolute;
    left: 0;
    top: 262px;
    width: 928px;
    height: 320px;
  }
  .sender {
    position: absolute;
    left: 0;
    width: 100%;
    bottom: 42px;
    text-align: center;
    font-size: 16px;
    line-height: 30px;
    color: var(--ink);
  }
  .footer-band {
    position: absolute;
    left: 0;
    bottom: 0;
    width: 928px;
    height: 34px;
    background: linear-gradient(180deg, var(--sage) 0%, var(--slate) 100%);
  }
</style>
</head>
<body>
<main class="letterhead">
  <header>
    <div class="wordmark">The Mariposa</div>
    <div class="header-mosaic" role="img" aria-label="Decorative mosaic of small squares in slate blue, sage grey, black and white"></div>
  </header>

  <svg class="content-frame" viewBox="0 262 928 320" aria-hidden="true">
    <polygon points="27,321 462,270 904,321 893,424 904,525 462,574 27,525 38,424"
             fill="none" stroke="var(--frame)" stroke-width="3"/>
  </svg>

  <footer>
    <p class="sender">
      412 Harwood Ln.&nbsp; Vancouver BC V6Z 3K8<br>
      Proudly managed by BrenTor Coastal. Lou Dane, Senior Property Manager
    </p>
    <div class="footer-band" role="img" aria-label="Decorative footer band of sage grey and slate blue triangles"></div>
  </footer>
</main>
</body>
</html>
```